Lanternfield Ministries Project Harvestline

I have a pop up display for inside tradeshows I would like for you to design. Here are the dimensions

pop up stand: 33(left side)+300+33cm(right side)

prodium: 1.04*2.2m

X stand: 60*160cm
I want to use the grayscale color wheel.
I want the backwall, xframes, and prodium to flow cohesively. I give you creative control on this project. Afterwards we will collaborate on the details. I want light gray from top gradually fading down to black which should be on the bottom.

Target Market(s)

Men and women from ages 16-59 yrs of age

Industry/Entity Type

Religious/ministry

Font styles to use
Serif

Colors

Designer to choose only greyscale colors for use in the design.

Requirements
Should not have
• N/a

```html
<!DOCTYPE html>
<html lang="en">
<head>
<meta charset="utf-8">
<title>Lanternfield Ministries – Backwall</title>
<link rel="stylesheet" href="https://fonts.googleapis.com/css2?family=Libre+Baskerville:wght@400;700&display=swap">
<style>
  :root {
    --paper-top: #d6d6d6;
    --paper-mid: #f4f4f4;
    --mist-light: #e6e6e6;
    --mist-dark: #c9c9c9;
    --ink: #111111;
    --band-edge: #ffffff;
    --band-text: #f2f2f2;
  }
  * { margin: 0; padding: 0; box-sizing: border-box; }
  html, body {
    width: 1200px;
    height: 835px;
    overflow: hidden;
    background: #ffffff;
  }
  .backwall {
    position: relative;
    width: 1200px;
    height: 835px;
    overflow: hidden;
    font-family: "Libre Baskerville", serif;
    color: var(--ink);
    background: radial-gradient(ellipse 70% 55% at 50% 30%, var(--paper-mid) 0%, var(--paper-top) 100%);
  }
  .backwall__art {
    position: absolute;
    inset: 0;
    width: 100%;
    height: 100%;
  }
  .brand {
    position: absolute;
    top: 152px;
    left: 0;
    width: 100%;
    text-align: center;
  }
  .brand__name {
    display: inline-flex;
    align-items: center;
    gap: 18px;
    font-size: 48px;
    font-weight: 400;
    line-height: 1;
  }
  .brand__mark {
    width: 36px;
    height: 36px;
    background: var(--ink);
    border-radius: 5px;
  }
  .brand__tagline {
    margin-top: 18px;
    font-size: 11px;
    font-weight: 400;
    letter-spacing: 5px;
  }
  .headline {
    position: absolute;
    top: 352px;
    left: 0;
    width: 100%;
    text-align: center;
  }
  .headline__lead {
    font-size: 30px;
    font-weight: 700;
    letter-spacing: 2px;
    line-height: 1;
  }
  .headline__main {
    margin-top: 12px;
    font-size: 56px;
    font-weight: 700;
    letter-spacing: 1px;
    line-height: 1;
  }
  .headline__welcome {
    margin-top: 16px;
    font-size: 15px;
    font-weight: 400;
    letter-spacing: 6px;
  }
  .belief {
    position: absolute;
    top: 552px;
    left: 0;
    width: 100%;
    text-align: center;
    font-size: 16px;
    font-weight: 700;
    line-height: 1.45;
    letter-spacing: 0.5px;
  }
  .site-url {
    position: absolute;
    top: 755px;
    left: 0;
    width: 100%;
    text-align: center;
    color: var(--band-text);
    font-size: 16px;
    font-weight: 400;
    letter-spacing: 2px;
  }
</style>
</head>
<body>
<main class="backwall">
  <svg class="backwall__art" viewBox="0 0 1200 835">
    <defs>
      <linearGradient id="mistFade" x1="0" y1="0" x2="0" y2="1">
        <stop offset="0" stop-color="#e6e6e6" stop-opacity="0"/>
        <stop offset="0.5" stop-color="#d2d2d2" stop-opacity="0.7"/>
        <stop offset="1" stop-color="#c9c9c9" stop-opacity="0.9"/>
      </linearGradient>
      <linearGradient id="bandFade" x1="0" y1="0" x2="0" y2="1">
        <stop offset="0" stop-color="#1c1c1c"/>
        <stop offset="0.3" stop-color="#050505"/>
        <stop offset="1" stop-color="#000000"/>
      </linearGradient>
    </defs>
    <rect x="0" y="420" width="1200" height="260" fill="url(#mistFade)" role="img" aria-label="Soft grey flowing swoosh decoration"/>
    <path d="M0,655 C300,615 560,705 800,692 C1000,682 1100,640 1200,612 L1200,835 L0,835 Z" fill="var(--band-edge)" aria-hidden="true"/>
    <path d="M0,668 C300,635 560,720 800,706 C1000,694 1100,654 1200,628 L1200,835 L0,835 Z" fill="url(#bandFade)" aria-hidden="true"/>
  </svg>

  <header class="brand">
    <div class="brand__name"><span class="brand__mark"></span>Lanternfield Ministries</div>
    <p class="brand__tagline">A HAND OUT IS A HAND UP</p>
  </header>

  <section class="headline">
    <p class="headline__lead">CARRYING OUT THE</p>
    <h1 class="headline__main">"GREAT COMMISSION"</h1>
    <p class="headline__welcome">WELCOME TO LANTERNFIELD MINISTRIES</p>
  </section>

  <p class="belief">WHERE WE BELIEVE<br>A HAND OUT, IS A HAND UP.</p>

  <p class="site-url">www.lanternfieldministries.com</p>
</main>
</body>
</html>
```